Stationary For Harbor Allies
Harbor Allies
Project: Stationary For Harbor Allies
Stationary For Harbor Allies - Consulting
Creative Brief
Professional
Lou Brannick
President
547 Marlow Ln Spring Branch, TX 78070
lbrannick@harborallies4.com
www.harborallies4.com
I will need letterhead and envelopes as well as business cards. Feel free to try different fonts.
quelnor42 quelnor42
Designers, Please focus more on the letterhead and envelopes than the business cards. Thanks!

```html
<!DOCTYPE html>
<html lang="en">
<head>
<meta charset="utf-8">
<title>Harbor Allies – Business Cards</title>
<link href="https://fonts.googleapis.com/css2?family=Open+Sans:wght@400;600;700&display=swap" rel="stylesheet">
<style>
  :root {
    --stage: #d6d6d6;
    --card: #ffffff;
    --navy: #2c4f8c;
    --navy-dark: #213d70;
    --faint: #c7d3e6;
    --ink: #555b66;
    --grey: #7a7f87;
  }
  * { margin: 0; padding: 0; box-sizing: border-box; }
  html, body {
    width: 1200px; height: 902px; overflow: hidden;
    background: var(--stage);
    font-family: "Open Sans", Arial, sans-serif;
  }
  .stage { position: relative; width: 1200px; height: 902px; }
  .card {
    position: absolute;
    width: 620px; height: 354px;
    background: var(--card);
    box-shadow: 0 10px 24px rgba(0,0,0,0.18);
    overflow: hidden;
  }
  .card--back { left: 480px; top: 64px; }
  .card--front { left: 110px; top: 474px; }

  .faint-mark {
    position: absolute;
    border-radius: 50%;
    background: var(--faint);
    opacity: 0.55;
  }
  .card--back .faint-mark { width: 230px; height: 230px; left: 250px; top: 36px; }
  .card--front .faint-mark { width: 120px; height: 120px; left: 400px; top: 18px; }

  .web-back {
    position: absolute; left: 70px; bottom: 42px;
    font-size: 17px; letter-spacing: 2px; color: var(--ink);
  }
  .web-back strong { font-weight: 700; }

  .brand {
    position: absolute; left: 40px; top: 120px;
    display: flex; align-items: center; gap: 12px;
  }
  .brand-dot { width: 44px; height: 44px; border-radius: 50%; background: var(--navy); }
  .brand-name { font-size: 28px; font-weight: 600; color: var(--navy); }

  .person { position: absolute; right: 40px; top: 138px; text-align: right; }
  .person-name { font-size: 20px; font-weight: 700; color: var(--navy); }
  .person-role { font-size: 17px; color: var(--grey); }

  .contact {
    position: absolute; left: 40px; top: 218px;
    list-style: none; font-size: 12.5px; color: var(--ink); line-height: 1.75;
  }
  .contact li { display: flex; align-items: center; gap: 8px; }
  .contact svg { width: 12px; height: 12px; fill: var(--navy); }

  .band {
    position: absolute; left: 0; right: 0; bottom: 0; height: 52px;
    background: linear-gradient(90deg, var(--navy), var(--navy-dark));
    display: flex; align-items: center; justify-content: flex-end;
    padding-right: 40px;
    color: #fff; font-size: 16px; letter-spacing: 2px;
  }
  .band-web strong { font-weight: 700; }
</style>
</head>
<body>
<main class="stage">
  <section class="card card--back" aria-label="Business card back">
    <div class="faint-mark" aria-hidden="true"></div>
    <p class="web-back">www.<strong>harborallies4</strong>.com</p>
  </section>

  <section class="card card--front" aria-label="Business card front">
    <div class="faint-mark" aria-hidden="true"></div>
    <div class="brand">
      <span class="brand-dot" aria-hidden="true"></span>
      <span class="brand-name">Harbor Allies</span>
    </div>
    <div class="person">
      <p class="person-name">Lou Brannick</p>
      <p class="person-role">President</p>
    </div>
    <ul class="contact">
      <li><svg viewBox="0 0 24 24" aria-hidden="true"><path d="M6.6 10.8a15 15 0 0 0 6.6 6.6l2.2-2.2a1 1 0 0 1 1-.25 11.4 11.4 0 0 0 3.6.57 1 1 0 0 1 1 1V20a1 1 0 0 1-1 1A17 17 0 0 1 3 4a1 1 0 0 1 1-1h3.5a1 1 0 0 1 1 1c0 1.25.2 2.45.57 3.57a1 1 0 0 1-.25 1z"/></svg>830.555.0142</li>
      <li><svg viewBox="0 0 24 24" aria-hidden="true"><path d="M2 5h20v14H2z M2 5l10 8 10-8" /></svg>lbrannick@harborallies4.com</li>
      <li><svg viewBox="0 0 24 24" aria-hidden="true"><path d="M12 2a7 7 0 0 0-7 7c0 5 7 13 7 13s7-8 7-13a7 7 0 0 0-7-7zm0 9.5A2.5 2.5 0 1 1 12 6.5a2.5 2.5 0 0 1 0 5z"/></svg>547 Marlow Ln Spring Branch, TX 78070</li>
    </ul>
    <div class="band"><p class="band-web">www.<strong>harborallies4</strong>.com</p></div>
  </section>
</main>
</body>
</html>
```